Holiday Rental Leaflet

Want a DL size double sided leaflet to distribute via local businesses, markets, family and friends
HOLIDAY RENTALCarrickalinga - 17 Brindle Street Sleeps 8-10 (2 Queen, 1 Double, 2 bunks), 4 bedrooms, BIR to all bedrooms 2 Bathrooms, one with bath, 2 toilets Open Plan Lounge/Dining/Kitchen area Dining Table for 8 peopleReverse cycle airconditionerSlow combustion wood heaterTV/DVD, CD/RadioKitchen has m/wave, oven, fridge/freezer, dishwasherBBQ providedTimber decking with 2 outside tables and 12 chairs Washing Machine and dryer provided One street back from beach Smoke free zone No Pets
For further information or to book contact Joan on 0491 287 306 or email joanfarrow27@velmarnet.com.au

Industry/Entity Type

Kitchen

Requirements
Nice to have
• Have sent a variety of photos of the house. No need to use all of them, pick out the most relevant for the leaflet.

```html
<!DOCTYPE html>
<html lang="en">
<head>
<meta charset="utf-8">
<title>Holiday Rental Leaflet – Carrickalinga</title>
<link href="https://fonts.googleapis.com/css2?family=Lilita+One&family=Arimo:wght@400;700&family=Nunito:wght@800;900&display=swap" rel="stylesheet">
<style>
  :root{
    --page:#ecebe8;
    --navy:#0d3f73;
    --blue:#1f8fd6;
    --blue-light:#3fb0ea;
    --blue-deep:#0f5e9c;
    --green-top:#7cad2b;
    --green-bottom:#b5d03f;
    --white:#ffffff;
  }
  *{box-sizing:border-box;margin:0;padding:0}
  html,body{width:1200px;height:1000px;overflow:hidden;background:var(--page)}
  .canvas{position:relative;width:1200px;height:1000px}
  .leaflet{position:absolute;top:32px;width:417px;height:874px;overflow:hidden;box-shadow:0 4px 14px rgba(0,0,0,.25)}
  .leaflet--front{left:138px}
  .leaflet--back{left:615px}
  .leaflet svg.art{position:absolute;inset:0}

  .title{position:absolute;left:0;right:0;text-align:center;white-space:nowrap}
  .title__main{top:22px;font-family:"Lilita One",sans-serif;font-size:47px;color:var(--navy);letter-spacing:.5px;
    text-shadow:-3px -3px 0 #fff,3px -3px 0 #fff,-3px 3px 0 #fff,3px 3px 0 #fff,0 3px 0 #fff,0 -3px 0 #fff,3px 0 0 #fff,-3px 0 0 #fff}
  .title__place{top:78px;font-family:"Nunito",sans-serif;font-weight:900;font-size:41px;color:var(--blue-deep);
    text-shadow:-2px -2px 0 #fff,2px -2px 0 #fff,-2px 2px 0 #fff,2px 2px 0 #fff}
  .title__street{top:128px;font-family:"Nunito",sans-serif;font-weight:900;font-size:30px;color:var(--blue);
    text-shadow:-2px -2px 0 #fff,2px -2px 0 #fff,-2px 2px 0 #fff,2px 2px 0 #fff}

  .tag{position:absolute;background:var(--blue);color:var(--white);font-family:"Arimo",sans-serif;white-space:nowrap;
    padding:0 14px 0 8px;display:flex;align-items:center;clip-path:polygon(0 0,100% 0,calc(100% - 10px) 50%,100% 100%,0 100%)}
  .tag--beach{left:20px;top:736px;height:30px;width:232px;font-size:16px}
  .tag--small{font-size:9.5px;font-weight:700;height:22px;padding-left:6px}
  .tag--decking{left:22px;top:35px;width:133px;height:26px;font-size:11px}
  .tag--fireplace{left:210px;top:250px;width:136px}
  .tag--lounge{left:210px;top:395px;width:136px}
  .tag--dining{left:210px;top:550px;width:136px}

  .features{position:absolute;left:20px;top:282px;width:212px;list-style:none;font-family:"Arimo",sans-serif;
    font-size:12.4px;line-height:15.8px;color:var(--white)}
  .features li{padding-left:16px;position:relative}
  .features li::before{content:"-";position:absolute;left:0}

  .contact{position:absolute;left:0;right:0;top:720px;font-family:"Arimo",sans-serif;color:var(--white)}
  .contact__lead{margin-left:22px;font-size:16px;line-height:20px}
  .contact__phone{margin-top:4px;text-align:center;font-weight:700;font-size:68px;line-height:70px;color:var(--blue);letter-spacing:-1px;white-space:nowrap;
    text-shadow:-3px -3px 0 #fff,3px -3px 0 #fff,-3px 3px 0 #fff,3px 3px 0 #fff,0 3px 0 #fff,0 -3px 0 #fff,3px 0 0 #fff,-3px 0 0 #fff}
  .contact__email{text-align:center;font-size:14px;margin-top:2px;padding-left:40px}
</style>
</head>
<body>
<div class="canvas">

  <section class="leaflet leaflet--front">
    <svg class="art" width="417" height="874" viewBox="0 0 417 874">
      <defs>
        <linearGradient id="greenTop" x1="0" y1="0" x2="0" y2="1">
          <stop offset="0" stop-color="var(--green-top)"/><stop offset="1" stop-color="var(--green-bottom)"/>
        </linearGradient>
        <linearGradient id="houseTone" x1="0" y1="0" x2="0" y2="1">
          <stop offset="0" stop-color="#dfe3e2"/><stop offset=".2" stop-color="#b9c0c2"/>
          <stop offset=".32" stop-color="#9a9f9e"/><stop offset=".42" stop-color="#8a7656"/>
          <stop offset=".55" stop-color="#4b4a44"/><stop offset=".64" stop-color="#8f9491"/>
          <stop offset=".72" stop-color="#7fa452"/><stop offset="1" stop-color="#6f9a45"/>
        </linearGradient>
        <linearGradient id="beachTone" x1="0" y1="0" x2="0" y2="1">
          <stop offset="0" stop-color="#cdd9e3"/><stop offset=".3" stop-color="#5f95b5"/>
          <stop offset=".45" stop-color="#3f7796"/><stop offset=".55" stop-color="#e4e1d8"/>
          <stop offset=".8" stop-color="#d4cbb7"/><stop offset="1" stop-color="#a89a7c"/>
        </linearGradient>
      </defs>
      <rect role="img" aria-label="Photo of the holiday house on stilts with lawn and sprinklers" x="0" y="180" width="417" height="500" fill="url(#houseTone)"/>
      <rect role="img" aria-label="Photo of the beach and sea below dunes" x="0" y="660" width="417" height="214" fill="url(#beachTone)"/>
      <path d="M0 0H417V210C330 170 240 200 150 215C90 225 40 215 0 190Z" fill="url(#greenTop)"/>
      <path d="M0 185C40 212 90 222 150 212C240 197 330 168 417 205V222C330 185 240 214 150 228C90 238 40 228 0 204Z" fill="var(--blue-deep)"/>
      <path d="M0 204C40 228 90 238 150 228C240 214 330 185 417 222V232C330 197 240 226 150 240C90 248 40 240 0 214Z" fill="var(--blue-light)"/>
      <path d="M0 650C70 690 160 700 250 680C320 665 370 655 417 670V700C370 685 320 692 250 706C160 722 70 712 0 680Z" fill="var(--blue-light)"/>
      <path d="M0 665C70 702 160 712 250 694C320 680 370 672 417 685V705C370 692 320 700 250 712C160 728 70 718 0 690Z" fill="var(--blue-deep)"/>
    </svg>
    <h1 class="title title__main">HOLIDAY RENTAL</h1>
    <p class="title title__place">Carrickalinga</p>
    <p class="title title__street">17 Brindle Street</p>
    <div class="tag tag--beach">One street back from beach</div>
  </section>

  <section class="leaflet leaflet--back">
    <svg class="art" width="417" height="874" viewBox="0 0 417 874">
      <defs>
        <linearGradient id="panelBlue" x1="0" y1="0" x2="1" y2="0">
          <stop offset="0" stop-color="var(--blue)"/><stop offset="1" stop-color="var(--blue-deep)"/>
        </linearGradient>
        <linearGradient id="deckTone" x1="0" y1="0" x2="0" y2="1">
          <stop offset="0" stop-color="#e3e8e6"/><stop offset=".18" stop-color="#7b7d72"/>
          <stop offset=".4" stop-color="#8d8a7c"/><stop offset=".6" stop-color="#4e524e"/>
          <stop offset=".85" stop-color="#5d6a52"/><stop offset="1" stop-color="#7d9b55"/>
        </linearGradient>
        <radialGradient id="fireTone" cx=".45" cy=".55" r=".7">
          <stop offset="0" stop-color="#6b4a3a"/><stop offset=".5" stop-color="#a07555"/><stop offset="1" stop-color="#c9a584"/>
        </radialGradient>
        <linearGradient id="loungeTone" x1="0" y1="0" x2="0" y2="1">
          <stop offset="0" stop-color="#b57a3f"/><stop offset=".4" stop-color="#6e4a30"/>
          <stop offset=".7" stop-color="#2a2624"/><stop offset="1" stop-color="#8c7b68"/>
        </linearGradient>
        <linearGradient id="diningTone" x1="0" y1="0" x2="1" y2="1">
          <stop offset="0" stop-color="#d9a266"/><stop offset=".5" stop-color="#c98a3e"/><stop offset="1" stop-color="#a8652a"/>
        </linearGradient>
        <linearGradient id="seaTone" x1="0" y1="0" x2="0" y2="1">
          <stop offset="0" stop-color="#d3e3ef"/><stop offset=".4" stop-color="#8fb5d0"/>
          <stop offset=".6" stop-color="#4f83a8"/><stop offset="1" stop-color="#3a6a8e"/>
        </linearGradient>
      </defs>
      <rect role="img" aria-label="Photo of the timber deck with umbrellas" x="0" y="0" width="417" height="250" fill="url(#deckTone)"/>
      <rect x="0" y="220" width="417" height="480" fill="url(#panelBlue)"/>
      <rect role="img" aria-label="Photo of the slow combustion fireplace" x="235" y="225" width="182" height="143" fill="url(#fireTone)"/>
      <rect role="img" aria-label="Photo of the lounge with leather sofas" x="235" y="372" width="182" height="168" fill="url(#loungeTone)"/>
      <rect role="img" aria-label="Photo of the dining table for eight" x="235" y="544" width="182" height="140" fill="url(#diningTone)"/>
      <rect role="img" aria-label="Photo of the sea and coastline" x="0" y="680" width="417" height="194" fill="url(#seaTone)"/>
      <path d="M0 215C60 250 130 260 200 245C280 228 350 215 417 240V262C350 235 280 246 200 262C130 276 60 266 0 236Z" fill="var(--white)"/>
      <path d="M235 368C300 378 360 360 417 340V372C360 392 300 380 235 372Z" fill="var(--white)"/>
      <path d="M235 540C300 548 360 535 417 520V544C360 560 300 552 235 544Z" fill="var(--white)"/>
      <rect x="231" y="230" width="4" height="450" fill="var(--white)"/>
      <path d="M0 700C90 670 180 650 260 660C330 668 380 680 417 665V688C380 704 330 692 260 684C180 674 90 694 0 724Z" fill="var(--white)"/>
    </svg>
    <div class="tag tag--decking">Timber decking</div>
    <div class="tag tag--small tag--fireplace">Fireplace</div>
    <div class="tag tag--small tag--lounge">Lounge area</div>
    <div class="tag tag--small tag--dining">Dining table for 8 people</div>
    <ul class="features">
      <li>Sleeps 8-10<br>(2 Queen, 1 Double, 2 bunks),<br>4 bedrooms</li>
      <li>BIR to all bedrooms</li>
      <li>2 Bathrooms<br>one with bath, 2 toilets</li>
      <li>Open Plan Lounge/Dining/<br>Kitchen area</li>
      <li>Dining Table for 8 people</li>
      <li>Reverse cycle airconditioner</li>
      <li>Slow combustion wood heater</li>
      <li>TV/DVD, CD/Radio</li>
      <li>Kitchen has m/wave, oven,<br>fridge/freezer, dishwasher</li>
      <li>BBQ provided</li>
      <li>Timber decking with 2 outside<br>tables and 12 chairs</li>
      <li>Washing Machine and dryer<br>provided</li>
      <li>One street back from beach</li>
      <li>Smoke free zone</li>
      <li>No Pets</li>
    </ul>
    <div class="contact">
      <p class="contact__lead">For further information or<br>to book contact Joan on</p>
      <p class="contact__phone">491 287 306</p>
      <p class="contact__email">joanfarrow27@velmarnet.com.au</p>
    </div>
  </section>

</div>
</body>
</html>
```